Passionate Homecare Agency Needs an "Employee News" Webpage Design

We are a homecare agency with more than 300 employees who provide personal care and assistance with the activities of daily living in clients’ homes. Our company slogan is “Someone you can depend on… Without question.” We strive to provide our clients with the highest quality, compassionate care possible, and we want our employees to feel inspired to do just that.

We are looking for an employee web page design to add to our existing website that makes our field employees feel connected to the company, is fun and energetic, and provides our caregivers with helpful information, employee news, and recognition. We want this to be a hub for communication and celebration, and also showcase our appreciation for all that they do!

We look forward to your designs! The sky's the limit!
Updates

Reason: Looking for a few more designs that fit our descriptions before making a final decision.

Target Market(s)

Our Employees

Industry/Entity Type

Home Health Care

Number of Pages Required

1 page

Colors

Designer to choose colors to be used in the design.

Requirements
Must have
• We would like to have sections like:
• -Employee of the Month/Week
• -Caregiver Tips and Tricks
• -Birthdays and Anniversaries
• -New Employees
• -Area to add links to our social media (Facebook, Instagram, Twitter)
• -etc!
Nice to have
• Bright colors and fun themes.

```html
<!DOCTYPE html>
<html lang="en">
<head>
<meta charset="utf-8">
<title>Harbor Care Group – Employee News</title>
<link href="https://fonts.googleapis.com/css2?family=PT+Sans:wght@400;700&family=Permanent+Marker&display=swap" rel="stylesheet">
<style>
:root{
  --blush:#f3e6e7;
  --pink:#f0217a;
  --teal:#2e8b84;
  --ink:#2b2b2b;
  --grey:#9a9a9a;
  --rule:#b9c6cc;
  --sky:#8ee9fb;
  --field:#f3e6e7;
}
*{box-sizing:border-box;margin:0;padding:0}
html,body{width:963px;height:1200px;overflow:hidden}
body{position:relative;font-family:"PT Sans",sans-serif;color:var(--ink);background:#fff}
.abs{position:absolute}
.script{font-family:"Permanent Marker",cursive;color:var(--teal);font-weight:400;font-variant:small-caps;letter-spacing:1px}

/* header */
.site-header{position:absolute;left:0;top:0;width:963px;height:160px;background:var(--blush);border-bottom:2px solid var(--rule)}
.brand{position:absolute;left:16px;top:40px;display:flex;align-items:center;gap:10px}
.brand-mark{width:50px;height:50px;background:var(--pink);border-radius:8px}
.brand-name{font-size:27px;color:var(--ink);font-weight:400;line-height:1}
.tagline{position:absolute;left:16px;top:111px;font-size:12.5px;font-style:italic}
.social{position:absolute;display:flex;gap:12px}
.social span{width:24px;height:24px;border-radius:50%;background:var(--grey)}
.social span.active{background:#111}
.header-social{left:642px;top:38px}
.phone{position:absolute;left:805px;top:36px;font-size:23px;font-weight:700;letter-spacing:.5px;color:#333}
.main-nav{position:absolute;left:391px;top:107px;display:flex;gap:22px;font-size:14px}
.main-nav a{color:var(--ink);text-decoration:none;padding-bottom:6px}
.main-nav a.current{border-bottom:2px solid var(--pink)}
.btn{position:absolute;top:98px;height:40px;border-radius:20px;font-size:13.5px;display:flex;align-items:center;justify-content:center}
.btn-signin{left:674px;width:112px;background:var(--pink);color:#fff}
.btn-new{left:810px;width:137px;border:2px solid var(--pink);color:var(--ink);background:transparent}

/* hero */
.hero{position:absolute;left:0;top:161px;width:963px;height:361px;background:linear-gradient(90deg,#e2e2e2,#ececec 60%,#f1f1f1)}
.hero-photo{position:absolute;left:0;top:0;width:401px;height:361px;background:linear-gradient(160deg,#cfd2d4,#9bd6ec 60%,#6cc8ea)}
.hero h2{position:absolute;left:481px;top:62px;font-size:34px}
.hero p{position:absolute;left:481px;top:114px;width:400px;font-size:13.6px;line-height:27.3px;color:#333}
.hero .arrow{position:absolute;top:152px}
.dots{position:absolute;left:872px;top:316px;display:flex;gap:9px}
.dots span{width:12px;height:12px;border-radius:50%;background:#bdbdbd}
.dots span.on{background:var(--pink)}

/* news */
.news h2{position:absolute;left:24px;top:544px;font-size:34px}
.news p{position:absolute;left:24px;top:599px;width:920px;font-size:13.6px;line-height:29px}
.more{color:var(--pink)}

/* panels */
.panels{position:absolute;left:0;top:737px;width:963px;height:234px;background:var(--blush);border-radius:6px 6px 0 0}
.panels .divider{position:absolute;left:513px;top:0;width:2px;height:234px;background:var(--rule)}
.panels h2{position:absolute;top:20px;font-size:27px}
.people{position:absolute;left:0;top:86px;width:513px}
.person{position:absolute;width:110px;text-align:center;font-size:12.4px;line-height:16px;color:#444}
.avatar{width:80px;height:80px;margin:0 auto 8px;border-radius:50%;border:2px solid var(--pink);background:radial-gradient(circle at 50% 40%,#b99b86,#4d5460)}
.panels .tips{position:absolute;left:546px;top:80px;width:390px;font-size:13.6px;line-height:29px}

/* footer */
.site-footer{position:absolute;left:0;top:971px;width:963px;height:229px;background:var(--sky)}
.site-footer h3{position:absolute;top:26px;font-size:20px;font-weight:700;color:#333}
.contact{position:absolute;left:32px;top:73px;font-size:13.5px;line-height:26px}
.hours{position:absolute;left:32px;top:202px;font-size:13px;font-weight:700}
.links{position:absolute;left:345px;top:73px;font-size:13.5px;list-style:none;line-height:33px}
.footer-social{left:345px;top:210px}
.form label{position:absolute;left:666px;font-size:13px}
.form .field{position:absolute;left:666px;width:266px;height:25px;background:var(--field);font-size:12.5px;color:#a9a9a9;padding:4px 7px}
</style>
</head>
<body>

<header class="site-header">
  <div class="brand"><span class="brand-mark"></span><span class="brand-name">Harbor Care Group</span></div>
  <p class="tagline">Someone you can depend on... Without question</p>
  <div class="social header-social"><span></span><span></span><span class="active"></span><span></span></div>
  <div class="phone">808-555-0147</div>
  <nav class="main-nav">
    <a class="current" href="#">Open Shifts</a>
    <a href="#">My Skills</a>
    <a href="#">Employee Forms</a>
  </nav>
  <a class="btn btn-signin">SIGN IN</a>
  <a class="btn btn-new">NEW EMPLOYEE</a>
</header>

<section class="hero">
  <div class="hero-photo" role="img" aria-label="Photo of a smiling caregiver in blue scrubs with a stethoscope"></div>
  <svg class="arrow" style="left:24px" width="30" height="56" viewBox="0 0 30 56"><polyline points="28,2 3,28 28,54" fill="none" stroke="var(--teal)" stroke-width="3"/></svg>
  <svg class="arrow" style="left:908px" width="30" height="56" viewBox="0 0 30 56"><polyline points="2,2 27,28 2,54" fill="none" stroke="var(--teal)" stroke-width="3"/></svg>
  <h2 class="script">Employee of the Week</h2>
  <p>Congratulations to Dana Reyes, Harbor’s Employee of the Weekf. Dana works with our Harbor Senior Living community and she is loved by staff and residents alike. Her beautiful bright smile and willing nature was noticed by many and earned her this weeks’ recognition for all the good work she does.</p>
  <div class="dots"><span class="on"></span><span></span><span></span></div>
</section>

<section class="news">
  <h2 class="script">Employee News</h2>
  <p>Lorem ipsum dolor sit amet, consectetur adipiscing elit. Etiam faucibus dolor metus, vel dapibus mi placerat id. Suspendisse rhoncus, felis at cursus maximus, tellus sem dictum quam, non ullamcorper purus ante eleifend risus. Vestibulum at orci et neque dignissim imperdiet quis sollicitudin dolor. Phasellus luctus iaculis porttitor. Vestibulum vel ornare est. Vivamus iaculis, metus sit amet elementum gravida, risus dolor sollicitudin tellus, id ullamcorper lacus leo id ex. Duis congue eros in turpis aliquam pulvinar...<span class="more">MORE</span></p>
</section>

<section class="panels">
  <h2 class="script" style="left:24px">Birthdays + Aniversaries</h2>
  <div class="people">
    <svg class="abs" style="left:12px;top:30px" width="18" height="34" viewBox="0 0 18 34"><polyline points="16,2 2,17 16,32" fill="none" stroke="var(--teal)" stroke-width="2"/></svg>
    <div class="person" style="left:26px;top:0"><div class="avatar" role="img" aria-label="Portrait of Priya Anand"></div>Priya Anand<br>April 17</div>
    <div class="person" style="left:142px;top:0"><div class="avatar" role="img" aria-label="Portrait of Edna Marsh"></div>Edna Marsh<br>32 years</div>
    <div class="person" style="left:260px;top:0"><div class="avatar" role="img" aria-label="Portrait of Cole Barrett"></div>Cole Barrett<br>3 years</div>
    <div class="person" style="left:376px;top:0"><div class="avatar" role="img" aria-label="Portrait of Mei Tanaka"></div>Mei Tanaka<br>April 29</div>
    <svg class="abs" style="left:486px;top:30px" width="18" height="34" viewBox="0 0 18 34"><polyline points="2,2 16,17 2,32" fill="none" stroke="var(--teal)" stroke-width="2"/></svg>
  </div>
  <div class="divider"></div>
  <h2 class="script" style="left:546px">Tips + Tricks</h2>
  <p class="tips">Suspendisse consectetur tempus laoreet. Maecenas sed est porta massa sodales sodales eu eget erat. Aliquam rhoncus neque quis erat tempus, sit amet volutpat felis molestie. Sed dictum nisl orci, non maximus...<span class="more">MORE</span></p>
</section>

<footer class="site-footer">
  <h3 style="left:32px">HARBOR CARE GROUP</h3>
  <p class="contact">4500 Makani Blvd. Suite 210<br>Honolulu, HI 96817<br>P: <b>808-555-0147</b><br>info@harborcare.com</p>
  <p class="hours">Business Hours</p>
  <ul class="links"><li>About us</li><li>Blog</li><li>Privacy Policy</li><li>Copyright ©2017</li></ul>
  <div class="social footer-social"><span></span><span></span><span class="active"></span><span></span></div>
  <h3 style="left:666px">Get in Touch</h3>
  <div class="form">
    <label style="top:75px">Name:</label>
    <div class="field" style="top:95px">John Smith</div>
    <label style="top:127px">Email:</label>
    <div class="field" style="top:147px">jsmith@email.com</div>
    <label style="top:177px">Message:</label>
    <div class="field" style="top:197px;height:40px">Message</div>
  </div>
</footer>

</body>
</html>
```